Personal Business Card

I am an award winning banjo player who plays with two different professional bands. My experiences include studio recordings for other artists and played the theme song for the Creature Channel's "Frontier Tundra Nights". I am ready to take my career to the next level and would like something that will look professional. it is important to me to have a banjo on the card. If possible my accomplishments to be put on back of card.

Industry/Entity Type

Artists

Contact Information for Business Card

Morgan Pell
cell 602-315-2860
email morganpellbanjo@quillpost.net

2008 AZ Banjo Champion
2008 Pinemeadow Banjo Champion
2010 AZ Banjo Champion
2010 Copper Creek Gathering Halvorn Banjo Champion
2010 Birchstone Hollow Fair Banjo Finalist

```html
<!DOCTYPE html>
<html lang="en">
<head>
<meta charset="utf-8">
<title>Morgan Pell — Business Card</title>
<link rel="stylesheet" href="https://fonts.googleapis.com/css2?family=Ubuntu:wght@400;700&display=swap">
<style>
  :root {
    --page-bg: #d9d9d9;
    --card-dark: #373737;
    --card-mid: #414141;
    --card-streak: #3c3c3c;
    --text-light: #f2f2f2;
    --text-soft: #e4e4e4;
    --photo-light: #8e8c8c;
    --photo-mid: #5e5a59;
    --photo-dark: #403b3a;
  }
  * { box-sizing: border-box; margin: 0; padding: 0; }
  html, body {
    width: 1200px;
    height: 1000px;
    overflow: hidden;
    background: var(--page-bg);
    font-family: "Ubuntu", sans-serif;
  }
  .sheet {
    width: 1200px;
    height: 1000px;
    display: flex;
    flex-direction: column;
    align-items: center;
    justify-content: space-evenly;
  }
  .card {
    position: relative;
    width: 800px;
    height: 457px;
    color: var(--text-light);
    background:
      repeating-linear-gradient(90deg,
        var(--card-dark) 0px, var(--card-streak) 3px,
        var(--card-mid) 7px, var(--card-dark) 11px),
      var(--card-dark);
    box-shadow: 0 2px 6px rgba(0,0,0,0.25);
  }

  /* Back of card: accomplishments */
  .awards { position: absolute; list-style: none; color: var(--text-soft); }
  .awards li { line-height: 1.45; }
  .awards--early { top: 26px; left: 30px; font-size: 15px; }
  .awards--recent { top: 300px; left: 300px; font-size: 18px; }

  /* Front of card: banjo photograph area and contact */
  .banjo-photo {
    position: absolute;
    left: 30px;
    top: 100px;
    width: 720px;
    height: 175px;
    border-radius: 14px;
    background: linear-gradient(90deg, var(--photo-light) 0%, var(--photo-mid) 45%, var(--photo-dark) 100%);
  }
  .contact {
    position: absolute;
    right: 70px;
    top: 290px;
    text-align: right;
  }
  .contact__name {
    font-weight: 700;
    font-size: 34px;
    margin-bottom: 22px;
  }
  .contact__line {
    font-size: 21px;
    line-height: 1.7;
  }
</style>
</head>
<body>
<main class="sheet">
  <section class="card card--back" aria-label="Card back">
    <ul class="awards awards--early">
      <li>2008 AZ Banjo Champion</li>
      <li>2008 Pinemeadow Banjo Champion</li>
    </ul>
    <ul class="awards awards--recent">
      <li>2010 AZ Banjo Champion</li>
      <li>2010 Copper Creek Gathering Halvorn Banjo Champion</li>
      <li>2010 Birchstone Hollow Fair Banjo Finalist</li>
    </ul>
  </section>

  <section class="card card--front" aria-label="Card front">
    <div class="banjo-photo" role="img" aria-label="Photograph of a five-string banjo lying diagonally across the card"></div>
    <div class="contact">
      <p class="contact__name">Morgan Pell</p>
      <p class="contact__line">cell :&nbsp; 602-315-2860</p>
      <p class="contact__line">email : morganpellbanjo@quillpost.net</p>
    </div>
  </section>
</main>
</body>
</html>
```